Corvell Law, PC Letterhead Design -- LAW FIRM

I am looking for a very elegant letterhead design for my personal injury law practice.
The letter head must have 4 different variations of the same thing meaning one design that has just a header, and another with a header and footer.
Elegance is key, I do not want it to be too bold. Please stay away from colors that are not black, white or gray or silver.
Please include a gradient style letterhead for the header while implementing the design of the logo found in folder #3
I have attached for you the logos and emblems for my company below.
In folders 1-4 you will find my actual logo.
In folder 5-6 you will find a shorter version of my logo, this can be implemented maybe in the footer + header design of the letter head (do not include this shortened version in the header).
In folders 7-8 you will find an emblem for my company.
Information that needs to be found on the letterhead is as follows:
A clearly written version of my company name: Corvell Law, PC
Address: 4718 Tamsden Avenue Suite #512, Beverly Hills, CA, 90210
Email: desmond@corvelllaw-example.com
Telephone number: 310-555-0147

```html
<!DOCTYPE html>
<html lang="en">
<head>
<meta charset="utf-8">
<title>Corvell Law, PC — Letterhead</title>
<link href="https://fonts.googleapis.com/css2?family=Outfit:wght@300;400&display=swap" rel="stylesheet">
<style>
  :root{
    --backdrop-top:#2b2b2b;
    --backdrop-mid:#404040;
    --paper:#ffffff;
    --ink:#1c1c1c;
    --silver:#c9c9c9;
    --steel:#999999;
    --footer-band:#8a8a8a;
    --emblem:#0a0a0a;
    --signature-tone:#ececec;
  }
  *{box-sizing:border-box;margin:0;padding:0}
  html,body{width:1200px;height:1200px;overflow:hidden}
  body{
    background:radial-gradient(ellipse at 50% 45%,var(--backdrop-mid) 0%,var(--backdrop-top) 80%);
    font-family:"Outfit",sans-serif;color:var(--ink);position:relative;
  }
  .sheet{position:absolute;top:211px;width:550px;height:778px;background:var(--paper);overflow:hidden}
  .sheet--plain{left:47px}
  .sheet--contact{left:609px}
  .header-art{position:absolute;left:0;top:0;width:550px;height:170px}
  .brand-mark{
    position:absolute;left:400px;top:44px;width:110px;height:110px;border-radius:50%;
    display:flex;flex-direction:column;align-items:center;justify-content:center;
    color:var(--paper);font-weight:300;font-size:15px;letter-spacing:.5px;line-height:1.2;text-align:center;
  }
  .contact-block{
    position:absolute;right:38px;top:173px;text-align:right;font-size:8.6px;line-height:10.5px;font-weight:400;
  }
  .contact-block .address{margin-bottom:4px}
  .contact-line{display:flex;justify-content:flex-end;align-items:center;gap:4px;height:12.5px}
  .contact-line svg{width:7px;height:7px}
  .letter{position:absolute;left:52px;top:225px;width:446px;font-size:10.4px;line-height:14.8px;font-weight:400}
  .recipient{margin-bottom:29px}
  .salutation{margin-bottom:15px}
  .letter-body p{text-align:justify}
  .signature{
    position:absolute;left:46px;top:603px;width:212px;height:54px;
    background:linear-gradient(90deg,var(--signature-tone),#f6f6f6);border-radius:3px;
  }
  .footer-band{position:absolute;left:0;bottom:0;width:550px;height:16px;background:var(--footer-band)}
</style>
</head>
<body>

<section class="sheet sheet--plain">
  <svg class="header-art" viewBox="0 0 550 170" aria-hidden="true">
    <rect width="550" height="170" fill="var(--silver)"/>
    <path d="M0 7 Q250 -6 505 95" fill="none" stroke="var(--paper)" stroke-width="3"/>
    <path d="M0 13 Q240 4 420 68 L410 72 Q230 28 0 36 Z" fill="var(--steel)"/>
    <path d="M0 36 Q230 28 410 72 Q485 100 550 127 L550 170 L0 170 Z" fill="var(--paper)"/>
    <path d="M505 96 Q530 108 550 118" fill="none" stroke="var(--paper)" stroke-width="3"/>
    <circle cx="455" cy="99" r="59" fill="var(--paper)"/>
    <circle cx="455" cy="99" r="55" fill="var(--emblem)"/>
  </svg>
  <div class="brand-mark"><span>Corvell</span><span>Law, PC</span></div>

  <div class="letter">
    <div class="recipient">Mr. John Doe<br>President<br>Halvern Accountants<br>111 Street Name,<br>City State, 12345</div>
    <div class="salutation">Dear</div>
    <div class="letter-body">
      <p>Lorem ipsum dolor sit amet, consectetur adipiscing elit. Aenean ut ipsum eget massa hendrerit vestibulum vel in velit. Donec pretium neque velit.</p>
      <p>Aliquam porta lectus nec mauris ornare venenatis. Vivamus non est turpis, et cursus sem. Mauris vehicula erat in diam auctor at bibendum nisl lacinia.</p>
      <p>Morbi imperdiet neque vehicula nunc convallis gravida. Vestibulum iaculis pretium placerat. Integer consequat, est sit amet facilisis eleifend, nibh nibh varius orci, eget dapibus arcu dui non purus. Pellentesque in magna mauris. Duis enim sapien, dictum vitae condimentum a, pulvinar vel lacus. Mauris et molestie nibh. Vestibulum vitae nulla at metus elementum porta sit amet interdum elit. Nulla sollicitudin neque eu nulla volutpat congue.</p>
      <p>Etiam pellentesque, velit id dapibus fermentum, turpis sapien ornare dui, ac tincidunt ligula odio congue purus. Nunc sed ante dui, in porta lectus. Cras nec sem lorem. In hac habitasse platea dictumst. Maecenas id diam quis dui porta tristique. Sed id egestas felis. Donec ullamcorper mattis posuere. Phasellus fermentum eleifend tortor vel dapibus. Vestibulum ante ipsum.</p>
    </div>
  </div>
  <div class="signature" role="img" aria-label="Handwritten signature of the sender"></div>
  <div class="footer-band"></div>
</section>

<section class="sheet sheet--contact">
  <svg class="header-art" viewBox="0 0 550 170" aria-hidden="true">
    <rect width="550" height="170" fill="var(--silver)"/>
    <path d="M0 7 Q250 -6 505 95" fill="none" stroke="var(--paper)" stroke-width="3"/>
    <path d="M0 13 Q240 4 420 68 L410 72 Q230 28 0 36 Z" fill="var(--steel)"/>
    <path d="M0 36 Q230 28 410 72 Q485 100 550 127 L550 170 L0 170 Z" fill="var(--paper)"/>
    <path d="M505 96 Q530 108 550 118" fill="none" stroke="var(--paper)" stroke-width="3"/>
    <circle cx="455" cy="99" r="59" fill="var(--paper)"/>
    <circle cx="455" cy="99" r="55" fill="var(--emblem)"/>
  </svg>
  <div class="brand-mark"><span>Corvell</span><span>Law, PC</span></div>

  <div class="contact-block">
    <div class="address">4718 Tamsden Avenue Suite #512,<br>Beverly Hills, CA, 90210</div>
    <div class="contact-line">desmond@corvelllaw-example.com
      <svg viewBox="0 0 10 10" aria-hidden="true"><rect x="0.5" y="2" width="9" height="6.5" fill="none" stroke="var(--ink)" stroke-width="1.2"/><path d="M0.5 2 L5 5.6 L9.5 2" fill="none" stroke="var(--ink)" stroke-width="1.2"/></svg>
    </div>
    <div class="contact-line">310-555-0147
      <svg viewBox="0 0 10 10" aria-hidden="true"><path d="M2 0.8 L3.8 2.8 L2.9 4 Q4.2 6.2 6 7.1 L7.2 6.2 L9.2 8 L8 9.4 Q4.5 9.2 2.2 6.6 Q0.4 4.3 0.6 2 Z" fill="var(--ink)"/></svg>
    </div>
  </div>

  <div class="letter">
    <div class="recipient">Mr. John Doe<br>President<br>Halvern Accountants<br>111 Street Name,<br>City State, 12345</div>
    <div class="salutation">Dear</div>
    <div class="letter-body">
      <p>Lorem ipsum dolor sit amet, consectetur adipiscing elit. Aenean ut ipsum eget massa hendrerit vestibulum vel in velit. Donec pretium neque velit.</p>
      <p>Aliquam porta lectus nec mauris ornare venenatis. Vivamus non est turpis, et cursus sem. Mauris vehicula erat in diam auctor at bibendum nisl lacinia.</p>
      <p>Morbi imperdiet neque vehicula nunc convallis gravida. Vestibulum iaculis pretium placerat. Integer consequat, est sit amet facilisis eleifend, nibh nibh varius orci, eget dapibus arcu dui non purus. Pellentesque in magna mauris. Duis enim sapien, dictum vitae condimentum a, pulvinar vel lacus. Mauris et molestie nibh. Vestibulum vitae nulla at metus elementum porta sit amet interdum elit. Nulla sollicitudin neque eu nulla volutpat congue.</p>
      <p>Etiam pellentesque, velit id dapibus fermentum, turpis sapien ornare dui, ac tincidunt ligula odio congue purus. Nunc sed ante dui, in porta lectus. Cras nec sem lorem. In hac habitasse platea dictumst. Maecenas id diam quis dui porta tristique. Sed id egestas felis. Donec ullamcorper mattis posuere. Phasellus fermentum eleifend tortor vel dapibus. Vestibulum ante ipsum.</p>
    </div>
  </div>
  <div class="signature" role="img" aria-label="Handwritten signature of the sender"></div>
  <div class="footer-band"></div>
</section>

</body>
</html>
```